Custom Truck shop New Business Card design

double sided business card including my new logo, brand colors and picking a font I attached, clean and modern look. I attached the old card for some reference. and would like to include the picture of the white truck attached. I would also like to have it with one of my employees info as well. (same info except name and title Brin Tolvay Service Writer)

Dale Porvick
Owner

address
48310 E Calloway Ridge Rd S
STE 217
Marsh Hollow, CO 80219

phone 720-555-0184

email dale@brokenspurrigs.example

website brokenspurrgis.example

social @brokenspurrigs

Target Market(s)

men 18-60

Industry/Entity Type

Automotive

Contact Information for Business Card

Dale Porvick Owner address 48310 E Calloway Ridge Rd S STE 217 Marsh Hollow, CO 80219 phone 720-555-0184 email dale@brokenspurrigs.example website brokenspurrgis.example social @brokenspurrigs

Font styles to use
Other font styles liked:
• fonts attached

Requirements
Must have
• new logo, orange #FC68D, Charcoal #333333
Nice to have
• the white truck

```html
<!DOCTYPE html>
<html lang="en">
<head>
<meta charset="utf-8">
<title>Broken Spur Rigs — Business Card</title>
<link rel="stylesheet" href="https://fonts.googleapis.com/css2?family=Poppins:ital,wght@0,300;0,400;0,500;0,600;1,900&display=swap">
<style>
  :root {
    --page: #f4f4f4;
    --card-dark: #0f0f0f;
    --card-mid: #2a2a2a;
    --charcoal: #333333;
    --orange: #fc6d2d;
    --orange-deep: #f2471f;
    --white: #ffffff;
    --silver: #c9c9c9;
  }
  * { box-sizing: border-box; margin: 0; padding: 0; }
  html, body {
    width: 722px; height: 1200px; overflow: hidden;
    background: var(--page);
    font-family: "Poppins", sans-serif;
  }
  .sheet {
    position: relative; width: 722px; height: 1200px;
  }
  .card {
    position: absolute; top: 320px;
    width: 320px; height: 561px;
    overflow: hidden;
    background: linear-gradient(180deg, var(--card-dark) 0%, #1e1e1e 45%, var(--card-mid) 100%);
    box-shadow: 0 10px 26px rgba(0,0,0,.35);
    color: var(--white);
  }
  .card--front { left: 28px; }
  .card--back { left: 374px; }

  .light-streak {
    position: absolute; inset: 0;
    background: linear-gradient(120deg, transparent 48%, rgba(255,255,255,.06) 48%, rgba(255,255,255,.06) 66%, transparent 66%);
  }
  .skyline {
    position: absolute; left: 0; right: 0;
    height: 90px;
    background: linear-gradient(180deg, rgba(70,70,70,0) 0%, rgba(70,70,70,.35) 55%, rgba(40,40,40,.2) 100%);
  }
  .card--front .skyline { top: 210px; }
  .card--back .skyline { top: 195px; }

  .brand {
    position: absolute; left: 0; right: 0;
    display: flex; flex-direction: column; align-items: center;
  }
  .brand__disc {
    border-radius: 50%;
    background: var(--white);
    border: 3px solid var(--charcoal);
    box-shadow: 0 0 0 2px var(--white);
  }
  .brand__name {
    font-weight: 600; color: var(--white);
    letter-spacing: .04em; text-transform: uppercase;
    white-space: nowrap;
  }
  .card--front .brand { top: 79px; }
  .card--front .brand__disc { width: 66px; height: 66px; }
  .card--front .brand__name { font-size: 21px; margin-top: 14px; }
  .card--back .brand { top: 26px; }
  .card--back .brand__disc { width: 46px; height: 46px; }
  .card--back .brand__name { font-size: 15px; margin-top: 9px; }

  .person {
    position: absolute; top: 130px; left: 0; right: 0;
    text-align: center;
  }
  .person__name {
    font-weight: 900; font-style: italic;
    font-size: 26px; line-height: 1; text-transform: uppercase;
    letter-spacing: .01em;
  }
  .person__surname { color: var(--orange); margin-left: 8px; }
  .person__title {
    font-weight: 400; font-size: 15px; letter-spacing: .02em;
    margin-top: 2px;
  }
  .person__rule {
    width: 56px; height: 2px; background: var(--orange);
    margin: 6px auto 0;
  }

  .contact {
    position: absolute; top: 192px; left: 0; right: 0;
    list-style: none; text-align: center;
  }
  .contact__item {
    display: flex; flex-direction: column; align-items: center;
    font-size: 13px; font-weight: 400; line-height: 1.25;
    margin-bottom: 9px;
  }
  .contact__icon {
    width: 16px; height: 16px; border-radius: 50%;
    background: var(--orange);
    display: flex; align-items: center; justify-content: center;
    margin-bottom: 4px;
  }
  .contact__icon svg { width: 10px; height: 10px; }
  .contact__item--address { text-align: left; }

  .hero { position: absolute; left: 0; top: 0; width: 320px; height: 561px; }
</style>
</head>
<body>
<main class="sheet">

  <section class="card card--front" aria-label="Card front">
    <div class="skyline" role="img" aria-label="Faint city skyline photograph"></div>
    <div class="light-streak"></div>
    <div class="brand">
      <span class="brand__disc"></span>
      <span class="brand__name">Broken Spur Rigs</span>
    </div>
    <svg class="hero" viewBox="0 0 320 561" aria-hidden="true">
      <defs>
        <linearGradient id="truckFront" x1="0" y1="0" x2="1" y2="0">
          <stop offset="0" stop-color="#b9b9b9"/>
          <stop offset=".6" stop-color="#8e8e8e"/>
          <stop offset="1" stop-color="#f2561f"/>
        </linearGradient>
      </defs>
      <circle cx="264" cy="468" r="160" fill="#1b1b1b" stroke="var(--orange)" stroke-width="6"/>
      <rect x="30" y="390" width="290" height="171" rx="6" fill="url(#truckFront)" role="img" aria-label="Photo of a lifted white pickup truck"/>
    </svg>
  </section>

  <section class="card card--back" aria-label="Card back">
    <div class="skyline" role="img" aria-label="Faint city skyline photograph"></div>
    <div class="brand">
      <span class="brand__disc"></span>
      <span class="brand__name">Broken Spur Rigs</span>
    </div>

    <div class="person">
      <h1 class="person__name">Dale<span class="person__surname">Porvick</span></h1>
      <p class="person__title">OWNER</p>
      <div class="person__rule"></div>
    </div>

    <ul class="contact">
      <li class="contact__item">
        <span class="contact__icon"><svg viewBox="0 0 10 10"><path d="M2.2 1.2l1.4 1.6-.8 1a5 5 0 0 0 2.4 2.4l1-.8 1.6 1.4-.9 1.3C4.6 8 2 5.4 1 2.1z" fill="#fff"/></svg></span>
        720-555-0184
      </li>
      <li class="contact__item">
        <span class="contact__icon"><svg viewBox="0 0 10 10"><rect x="1.5" y="2.5" width="7" height="5" fill="#fff"/><path d="M1.5 2.5L5 5.5l3.5-3" fill="none" stroke="#fc6d2d" stroke-width=".8"/></svg></span>
        dale@brokenspurrigs.example
      </li>
      <li class="contact__item contact__item--address">
        <span class="contact__icon" style="align-self:center"><svg viewBox="0 0 10 10"><path d="M5 9.5C3 7 2 5.4 2 4a3 3 0 0 1 6 0c0 1.4-1 3-3 5.5z" fill="#fff"/><circle cx="5" cy="4" r="1.1" fill="#fc6d2d"/></svg></span>
        <span>48310 E Calloway Ridge Rd S STE<br>217 Marsh Hollow, CO 80219</span>
      </li>
    </ul>

    <svg class="hero" viewBox="0 0 320 561" aria-hidden="true">
      <defs>
        <linearGradient id="truckBack" x1="0" y1="0" x2="1" y2="0">
          <stop offset="0" stop-color="#b9b9b9"/>
          <stop offset=".6" stop-color="#8e8e8e"/>
          <stop offset="1" stop-color="#f2561f"/>
        </linearGradient>
      </defs>
      <circle cx="256" cy="479" r="147" fill="#1b1b1b" stroke="var(--orange)" stroke-width="6"/>
      <rect x="52" y="410" width="268" height="151" rx="6" fill="url(#truckBack)" role="img" aria-label="Photo of a lifted white pickup truck"/>
    </svg>
  </section>

</main>
</body>
</html>
```